Personal training and nutrition business needs business card design

We need a business card that outlays our services and invites potential customers to join our team and take the first step to a healthier and more enjoyable life. We cater for any level of fitness and specialize in weight loss and conditioning, strength training, muscle gain and strength endurance. Whether you are just starting off or need some help getting to the next level of your journey we are here to get the job done.
We specialize in one on one or one on two personal training sessions and each program will be custom made to suit individual fitness goals of our clients

```html
<!DOCTYPE html>
<html lang="en">
<head>
<meta charset="utf-8">
<title>Stride &amp; Rise — Business Card</title>
<link rel="stylesheet" href="https://fonts.googleapis.com/css2?family=Raleway:wght@400;600;800&family=Lato:wght@400&family=Oswald:wght@500&display=swap">
<style>
  :root {
    --bg: #e4e4e4;
    --purple-light: #b063a8;
    --purple-mid: #9656a4;
    --purple-deep: #7d4c9f;
    --accent: #8e4fa6;
    --tagline: #a1559f;
    --ink: #1c1c1c;
    --white: #ffffff;
  }
  * { margin: 0; padding: 0; box-sizing: border-box; }
  html, body { width: 1200px; height: 900px; overflow: hidden; background: var(--bg); }
  .stage { position: relative; width: 1200px; height: 900px; }

  .card {
    position: absolute; top: 216px; width: 309px; height: 501px;
    box-shadow: 2px 3px 4px rgba(0,0,0,.45);
  }
  .card--front {
    left: 279px;
    border-radius: 0 62px 0 62px;
    background: linear-gradient(150deg, var(--purple-light) 0%, var(--purple-mid) 45%, var(--purple-deep) 75%, var(--purple-light) 100%);
    color: var(--white);
    text-align: center;
  }
  .card--back {
    left: 617px;
    border-radius: 62px 0 62px 0;
    background: var(--white);
  }

  .brand { position: absolute; left: 0; right: 0; text-align: center; }
  .brand__dot { display: block; margin: 0 auto 18px; border-radius: 50%; }
  .card--front .brand { top: 120px; }
  .card--front .brand__dot { width: 64px; height: 64px; background: var(--white); }
  .card--back .brand { top: 72px; }
  .card--back .brand__dot { width: 64px; height: 64px; background: var(--accent); }
  .brand__name {
    font-family: "Raleway", sans-serif; font-weight: 800;
    font-size: 34px; line-height: 36px; letter-spacing: 1px; text-transform: uppercase;
  }
  .card--front .brand__name { color: var(--white); }
  .card--back .brand__name { color: var(--ink); }
  .brand__tagline {
    font-family: "Oswald", sans-serif; font-weight: 500;
    font-size: 8.5px; letter-spacing: 1px; text-transform: uppercase; margin-top: 12px;
  }
  .card--front .brand__tagline { color: var(--white); }
  .card--back .brand__tagline { color: var(--tagline); }

  .services {
    position: absolute; left: 0; right: 0; top: 374px; list-style: none;
    font-family: "Raleway", sans-serif; font-weight: 400; font-size: 15px; line-height: 21px;
    text-transform: uppercase;
  }

  .contact { position: absolute; left: 37px; top: 294px; font-family: "Lato", sans-serif; color: var(--ink); }
  .contact__name {
    font-family: "Raleway", sans-serif; font-weight: 600; font-size: 19px; line-height: 20px;
    color: var(--accent); text-transform: uppercase;
  }
  .contact__role { font-size: 14.5px; line-height: 18px; margin-bottom: 12px; }
  .contact__list { list-style: none; font-size: 14.5px; line-height: 19.5px; }
  .contact__list li { display: flex; align-items: center; gap: 6px; }
  .contact__list svg { width: 14px; height: 14px; flex: none; }
  .contact__list .contact__address { align-items: flex-start; margin-top: 16px; line-height: 18px; }
  .web-accent { color: var(--accent); }
</style>
</head>
<body>
<main class="stage">
  <section class="card card--front" aria-label="Card front">
    <div class="brand">
      <span class="brand__dot"></span>
      <div class="brand__name">Stride<br>&amp; Rise</div>
      <div class="brand__tagline">Personal training.&nbsp; Nutrition. Motivation</div>
    </div>
    <ul class="services">
      <li>Weight loss &amp; conditioning</li>
      <li>Strength training</li>
      <li>Muscle gain</li>
      <li>Strength endurance</li>
    </ul>
  </section>

  <section class="card card--back" aria-label="Card back">
    <div class="brand">
      <span class="brand__dot"></span>
      <div class="brand__name">Stride<br>&amp; Rise</div>
      <div class="brand__tagline">Personal training.&nbsp; Nutrition. Motivation</div>
    </div>
    <div class="contact">
      <div class="contact__name">Daniel Reyes</div>
      <div class="contact__role">Managing Director</div>
      <ul class="contact__list">
        <li>
          <svg viewBox="0 0 16 16" aria-hidden="true"><path d="M3 1.5l2.5 0 1.2 3.2-1.6 1.2a8 8 0 0 0 5 5l1.2-1.6 3.2 1.2 0 2.5c0 .8-.7 1.5-1.5 1.5A12.5 12.5 0 0 1 1.5 3c0-.8.7-1.5 1.5-1.5z" fill="none" stroke="#8e4fa6" stroke-width="1.6"/></svg>
          044-987 654 321
        </li>
        <li>
          <svg viewBox="0 0 16 16" aria-hidden="true"><rect x="1" y="3" width="14" height="10" fill="#8e4fa6"/><path d="M1 3l7 6 7-6M1 13l5-5M15 13l-5-5" fill="none" stroke="#fff" stroke-width="1.1"/></svg>
          hello@strideandrise.com
        </li>
        <li>
          <svg viewBox="0 0 16 16" aria-hidden="true"><g fill="none" stroke="#8e4fa6" stroke-width="1.2"><circle cx="8" cy="8" r="6.5"/><ellipse cx="8" cy="8" rx="3" ry="6.5"/><path d="M1.5 8h13M2.5 4.8h11M2.5 11.2h11"/></g></svg>
          <span>www.<span class="web-accent">strideandrise</span>.com</span>
        </li>
        <li class="contact__address">
          <svg viewBox="0 0 16 16" aria-hidden="true"><path d="M8 1a5 5 0 0 0-5 5c0 3.8 5 9 5 9s5-5.2 5-9a5 5 0 0 0-5-5z" fill="#8e4fa6"/><circle cx="8" cy="6" r="1.8" fill="#fff"/></svg>
          <span>88 Harbour Lane<br>Eastvale, 20417</span>
        </li>
      </ul>
    </div>
  </section>
</main>
</body>
</html>
```